Kitesurf Weather Forecast Application Needs an Advertising Banner

We need an Advertising Banner for our iOS Kitesurf Weather Forecast Application. The application name is GustMapper and you can download it from the Plum Depot.

https://apps.plumdepot-market.com/app/gustmapper-breeze-and-sky-outlook/id804417392?mt=8

The banner should have the logo of our application, which can be either found from the Plum Depot or uploaded on this post. It should describe what our app does with either words or graphic story. GustMapper is a weather forecast application for Kitesurfers. As the banner is small, animated gifs will also be considered.

We need the following sizes 320x50 and 728x90. The banner will be uploaded to tavlo. Tavlo accepts images in PNG, JPEG and GIF. We want it in one of the formats that can be uploaded to TavLo and vector .ai so we can make changed if necessary in the future.

On tap the banner will open Plum Depot on the user's device and present GustMapper.

06/09. I added a screenshot from an application that the banner will be added. The screenshot is from an Lumafon 4 Max (it is from a big device). The red area on the bottom is where the advert will go and it should be readable.

Target Market(s)

Banner will be displayed in other iOS Applications. One of them is Rigging Reckoner https://apps.plumdepot-market.com/us/app/rigging-reckoner/id937206148?mt=8

Industry/Entity Type

Advertising

Font styles to use
Other font styles liked:
• San Francisco

Requirements
Must have
• GustMapper logo and communicate a clear message on what the application does. GustMapper is a weather forecast application for Kitesurfers. If you want to find more information please visit the PlumDepot link provided.
Nice to have
• Animated gif will be nice to have, as the banner is small and it maybe difficult to communicate the message required.
Should not have
• We prefer something minimal and along the lines of our application design.

```html
<!DOCTYPE html>
<html lang="en">
<head>
<meta charset="utf-8">
<title>GustMapper advertising banners</title>
<link rel="stylesheet" href="https://fonts.googleapis.com/css2?family=Inter:wght@300;400;700;800&display=swap">
<style>
  :root {
    --backdrop-top: #2a2624;
    --backdrop-mid: #2e2a27;
    --backdrop-sea: #211f1e;
    --sky-top: #c9b7a2;
    --sky-low: #9c8e86;
    --sea-top: #3a3c45;
    --sea-low: #23262c;
    --purple: rgba(110, 66, 206, 0.92);
    --band: rgba(70, 70, 70, 0.55);
    --lime: #d6f53c;
    --cyan: #3ee8e0;
    --white: #ffffff;
    --badge: #0b0b0b;
    --badge-line: #9a9a9a;
  }
  * { margin: 0; padding: 0; box-sizing: border-box; }
  html, body { width: 1200px; height: 1187px; overflow: hidden; }
  body { font-family: "Inter", sans-serif; position: relative; background: var(--backdrop-mid); }

  .backdrop {
    position: absolute; inset: 0;
    background: linear-gradient(180deg, var(--backdrop-top) 0%, var(--backdrop-mid) 75%, var(--backdrop-sea) 79%, #1c1b1b 100%);
  }

  .banner { position: absolute; overflow: hidden; }
  .banner-scene {
    position: absolute; inset: 0;
    background: linear-gradient(180deg, var(--sky-top) 0%, var(--sky-low) 55%, var(--sea-top) 58%, var(--sea-low) 100%);
  }

  .headline-box {
    position: absolute; background: var(--purple); color: var(--lime);
    font-weight: 300; white-space: nowrap; display: flex; align-items: center;
  }
  .headline-box b { font-weight: 700; }
  .tagline {
    position: absolute; left: 0; background: var(--band); color: var(--lime);
    font-weight: 400; white-space: nowrap; display: flex; align-items: center;
  }
  .tagline .accent, .cta-box .accent { color: var(--cyan); }
  .cta-box {
    position: absolute; background: var(--purple); color: var(--lime);
    font-weight: 800; white-space: nowrap; display: flex; align-items: center;
  }
  .brand-dot { position: absolute; border-radius: 50%; background: var(--white); }
  .store-badge {
    position: absolute; background: var(--badge); border: 1px solid var(--badge-line); border-radius: 5px;
  }

  /* 728 x 90 */
  .banner-large { left: 244px; top: 438px; width: 728px; height: 90px; }
  .banner-large .headline-box { left: 0; top: 28px; height: 34px; padding: 0 6px; font-size: 19px; }
  .banner-large .tagline { top: 67px; height: 23px; padding: 0 6px; font-size: 12px; }
  .banner-large .cta-box { right: 0; top: 10px; height: 33px; padding: 0 7px 0 12px; font-size: 16px; }
  .banner-large .brand-dot { left: 451px; top: 17px; width: 20px; height: 20px; }
  .banner-large .store-badge { left: 620px; top: 57px; width: 98px; height: 29px; }

  /* 320 x 50 */
  .banner-small { left: 651px; top: 587px; width: 320px; height: 51px; }
  .banner-small .headline-box { left: 0; top: 13px; height: 21px; padding: 0 7px; font-size: 12px; }
  .banner-small .tagline { top: 34px; height: 17px; padding: 0 7px; font-size: 11px; }
  .banner-small .brand-dot { left: 253px; top: 5px; width: 14px; height: 14px; }
  .banner-small .store-badge { left: 245px; top: 26px; width: 68px; height: 20px; border-radius: 4px; }
</style>
</head>
<body>
  <div class="backdrop" role="img" aria-label="Dusk photograph of kitesurfers and colourful kites over the sea"></div>

  <a class="banner banner-large" aria-label="GustMapper 728 by 90 banner">
    <div class="banner-scene" role="img" aria-label="Sunset beach photo with kites in the sky and kitesurfers on the waves"></div>
    <div class="headline-box">Know&nbsp;<b>WHEN</b>&nbsp;to surf.&nbsp;<b>ALWAYS.</b></div>
    <div class="tagline">Best&nbsp;<span class="accent">weather app</span>&nbsp;for kitesurfers</div>
    <span class="brand-dot"></span>
    <div class="cta-box">Get&nbsp;<span class="accent">GustMapper</span>&nbsp;&amp; Let’s SURF!</div>
    <span class="store-badge" aria-label="Plum Depot download badge"></span>
  </a>

  <a class="banner banner-small" aria-label="GustMapper 320 by 50 banner">
    <div class="banner-scene" role="img" aria-label="Sunset beach photo with kites in the sky and kitesurfers on the waves"></div>
    <div class="headline-box">Know&nbsp;<b>WHEN</b>&nbsp;to surf.&nbsp;<b>ALWAYS.</b></div>
    <div class="tagline">Best&nbsp;<span class="accent">weather app</span>&nbsp;for kitesurfers</div>
    <span class="brand-dot"></span>
    <span class="store-badge" aria-label="Plum Depot download badge"></span>
  </a>
</body>
</html>
```